CartPulse Brochure

I need a design for an informational brochure for one of our products we are launching called CartPulse. Basically the product is a bunch of sensor mounted on retail shelves that scan when a customer selects products and what products they are. This is new technology, and aimed at the retail and research sectors.
We need a brochure that can reflect technology, retail, or research. My company specialises in creating new technology, software, and hardware for the market research, and retail sectors.
The brochure will have some text and images of the product within it.
I do like matte black, blue etc reflecting technology, but feel free to use your imagination.
The design should communicate new technology.. customers picking up products off a shelf, research etc.
The product itself involves a base electronic box that sits under the shelves, and gathers information that the sensors mounted on the shelves picks up.. this data is then sent back to our online dashboard for clients to review.

Industry/Entity Type

Electronic

Requirements
Must have
• Prefer either a square brochure, 2 pages
Or, maybe an A4 brochure, 2 sided
or do you have any ideas for a funky tech looking brochure

```html
<!DOCTYPE html>
<html lang="en">
<head>
<meta charset="utf-8">
<title>CartPulse Information Brochure</title>
<link href="https://fonts.googleapis.com/css2?family=Jost:wght@400;500&display=swap" rel="stylesheet">
<style>
  :root {
    --blue-bright: #05a9ec;
    --blue-mid: #0a7fb6;
    --blue-deep: #0c4d6a;
    --teal-dark: #0f3346;
    --matte-black: #141414;
    --paper: #fafafa;
    --ink-grey: #555a5e;
    --white: #ffffff;
  }
  * { margin: 0; padding: 0; box-sizing: border-box; }
  html, body { width: 1200px; height: 848px; overflow: hidden; }
  body {
    background: var(--matte-black);
    font-family: "Jost", "Futura", sans-serif;
    color: var(--white);
    position: relative;
  }
  .panel { position: absolute; }

  /* Cover: product */
  .panel-product {
    left: 0; top: 0; width: 598px; height: 509px;
    background: linear-gradient(110deg, var(--blue-bright) 0%, var(--blue-mid) 55%, var(--blue-deep) 100%);
    text-align: center;
  }
  .product-visual {
    position: absolute; left: 160px; top: 78px; width: 275px; height: 252px;
    background: radial-gradient(circle at 60% 60%, #3a3f44 0%, #1b1d20 60%, #0c0d0f 100%);
    border-radius: 6px;
  }
  .product-title {
    position: absolute; left: 0; right: 0; top: 370px;
    font-size: 26px; font-weight: 400; letter-spacing: 0.5px;
  }
  .product-lead {
    position: absolute; left: 0; right: 0; top: 428px;
    font-size: 19.5px; line-height: 24px;
  }

  /* Cover: title */
  .panel-title {
    left: 598px; top: 0; width: 602px; height: 509px;
    background: linear-gradient(215deg, var(--matte-black) 0%, #0d2b3b 35%, var(--blue-mid) 75%, var(--blue-bright) 100%);
  }
  .brochure-heading {
    position: absolute; right: 20px; top: 72px;
    font-size: 32px; font-weight: 400;
  }
  .sector-list {
    position: absolute; left: 156px; top: 295px;
    font-size: 19px; line-height: 24px;
  }

  /* Back pages */
  .back-pages { left: 0; top: 530px; width: 1200px; height: 318px; }
  .contact {
    position: absolute; left: 0; top: 566px; width: 598px;
    text-align: center;
  }
  .contact-heading { font-size: 34px; font-weight: 400; margin-bottom: 20px; }
  .contact-lines { font-size: 19px; line-height: 24px; }
  .contact-lines + .contact-lines { margin-top: 24px; }

  .brand-mark {
    position: absolute; left: 842px; top: 617px;
    display: flex; align-items: center; gap: 12px;
  }
  .brand-dot { width: 26px; height: 26px; border-radius: 50%; background: var(--blue-bright); }
  .brand-name {
    font-size: 25px; font-weight: 400; letter-spacing: 0.5px; color: var(--ink-grey);
  }
</style>
</head>
<body>
  <section class="panel panel-product">
    <div class="product-visual" role="img" aria-label="Boxed software package with disc, glossy black product render"></div>
    <h2 class="product-title">PREMIUM SOFTWARE PACKAGE</h2>
    <p class="product-lead">We need a brochure that can reflect technology,<br>retail, or research.</p>
  </section>

  <section class="panel panel-title">
    <h1 class="brochure-heading">Information Brochure</h1>
    <p class="sector-list">Software Hardware and<br>Retail Sectors</p>
  </section>

  <svg class="panel back-pages" viewBox="0 0 1200 318" width="1200" height="318" aria-hidden="true">
    <defs>
      <linearGradient id="backBlue" x1="0" y1="0" x2="1" y2="0">
        <stop offset="0" stop-color="#05a9ec"/>
        <stop offset="0.5" stop-color="#0a7fb6"/>
        <stop offset="1" stop-color="#0f3346"/>
      </linearGradient>
    </defs>
    <polygon points="0,0 598,0 973,318 0,318" fill="url(#backBlue)"/>
    <polygon points="598,0 1200,0 1200,318 973,318" fill="#fafafa"/>
    <rect x="0" y="265" width="598" height="53" fill="#141414"/>
  </svg>

  <address class="contact" style="font-style: normal;">
    <h2 class="contact-heading">For More Details:</h2>
    <p class="contact-lines">CartPulse<br>Lakeview, USA<br>01555 019, 5550142876</p>
    <p class="contact-lines">info@cartpulse.com<br>www.cartpulse.com</p>
  </address>

  <div class="brand-mark">
    <span class="brand-dot"></span>
    <span class="brand-name">CARTPULSE</span>
  </div>
</body>
</html>
```